Save our Business Card - We need your help

We need a fresh look on our business cards. We like it as it is, but it's not quite getting the 'wow' effect that we desire.
We're a tech startup building a cloud based solution for retailers consisting of Point of Sale, Inventory management and CRM.
The design should communicate a sense of a company that cares about the little things, design and relationships.
You can have a look at our website www.brimvale.com to get a feel for what we're like. Please feel free to message us for any further clarification
Our Customers are retail busines owners, cafe owners, other startups etc.
Building

```html
<!DOCTYPE html>
<html lang="en">
<head>
<meta charset="utf-8">
<title>Brimvale Business Card</title>
<link href="https://fonts.googleapis.com/css2?family=Open+Sans:wght@400;600;700&display=swap" rel="stylesheet">
<style>
  :root {
    --backdrop: #4a423d;
    --card: #1c1c1d;
    --card-back: #141414;
    --orange: #f39323;
    --white: #f4f4f4;
    --muted: #cfcfcf;
    --emboss: #3a3a3a;
    --divider: #5a4a35;
  }
  * { margin: 0; padding: 0; box-sizing: border-box; }
  html, body {
    width: 1200px; height: 804px; overflow: hidden;
    background: var(--backdrop);
    font-family: "Open Sans", Arial, sans-serif;
  }
  .stage {
    position: relative; width: 1200px; height: 804px;
    display: flex; align-items: center; justify-content: center; gap: 40px;
  }
  .card {
    position: relative; width: 540px; height: 310px;
    border-radius: 4px;
    box-shadow: 0 12px 30px rgba(0,0,0,.45);
  }
  .card--back { background: var(--card-back); }
  .card--front { background: var(--card); }

  .back-brand {
    position: absolute; left: 60px; top: 110px;
    display: flex; align-items: center; gap: 20px;
  }
  .back-brand .brand-square { width: 86px; height: 86px; background: var(--emboss); }
  .back-brand .brand-name {
    font-size: 62px; font-weight: 700; color: var(--emboss); letter-spacing: -1px;
  }

  .front-brand {
    position: absolute; left: 34px; top: 124px;
    display: flex; align-items: center; gap: 12px;
  }
  .front-brand .brand-square { width: 58px; height: 58px; background: var(--orange); }
  .front-brand .brand-name {
    font-size: 38px; font-weight: 700; color: var(--orange); letter-spacing: -0.5px;
  }

  .divider {
    position: absolute; left: 296px; top: 98px; width: 1px; height: 120px;
    background: linear-gradient(transparent, var(--divider), transparent);
  }

  .contact { position: absolute; left: 312px; top: 58px; color: var(--white); }
  .contact .person-name { font-size: 24px; font-weight: 700; color: var(--orange); line-height: 1.1; }
  .contact .person-title { font-size: 13px; color: var(--muted); margin-bottom: 10px; }
  .contact .address { font-size: 14px; line-height: 1.35; margin-bottom: 8px; }
  .contact ul { list-style: none; font-size: 14px; line-height: 1.5; }
  .contact li { display: flex; align-items: center; gap: 7px; }
  .contact svg { width: 12px; height: 12px; fill: var(--orange); flex: none; }
</style>
</head>
<body>
<main class="stage">
  <section class="card card--back" aria-label="Card back">
    <div class="back-brand">
      <span class="brand-square"></span>
      <span class="brand-name">Brimvale</span>
    </div>
  </section>

  <section class="card card--front" aria-label="Card front">
    <div class="front-brand">
      <span class="brand-square"></span>
      <span class="brand-name">Brimvale</span>
    </div>
    <div class="divider"></div>
    <div class="contact">
      <p class="person-name">Daniel Whitford</p>
      <p class="person-title">Managing Member</p>
      <p class="address">2280 Harbor Lane,<br>Fresno, CA 93721</p>
      <ul>
        <li><svg viewBox="0 0 12 12"><path d="M2.5 1l2 2.2-1 1.3a7 7 0 0 0 4 4l1.3-1L11 9.5 9.6 11C5 11 1 7 1 2.4z"/></svg>(559) 412-3380</li>
        <li><svg viewBox="0 0 12 12"><path d="M3 1h5v3H3zM1 5h10v5H9v1H3v-1H1zm3 3v2h4V8z"/></svg>(559) 412-3381</li>
        <li><svg viewBox="0 0 12 12"><path d="M3.5 0h5a1 1 0 0 1 1 1v10a1 1 0 0 1-1 1h-5a1 1 0 0 1-1-1V1a1 1 0 0 1 1-1zm.5 2v7h4V2z"/></svg>(559) 708-2145</li>
        <li><svg viewBox="0 0 12 12"><path d="M0 2h12v1L6 7 0 3zm0 2.3l6 4 6-4V10H0z"/></svg>daniel@brimvale.com</li>
        <li><svg viewBox="0 0 12 12"><path d="M6 0a6 6 0 1 0 0 12A6 6 0 0 0 6 0zm0 1.2c.7.7 1.2 2 1.3 3.3H4.7C4.8 3.2 5.3 1.9 6 1.2zM1.3 5.5h2.4c0 1.2.3 2.4.9 3.4a4.8 4.8 0 0 1-3.3-3.4zm3.4 0h2.6c-.1 1.3-.6 2.6-1.3 3.3-.7-.7-1.2-2-1.3-3.3zm3.6 0h2.4a4.8 4.8 0 0 1-3.3 3.4c.6-1 .9-2.2.9-3.4zm2.4-1H8.3c0-1.2-.3-2.4-.9-3.4a4.8 4.8 0 0 1 3.3 3.4zm-7 0H1.3a4.8 4.8 0 0 1 3.3-3.4c-.6 1-.9 2.2-.9 3.4z"/></svg>www.brimvale.com</li>
      </ul>
    </div>
  </section>
</main>
</body>
</html>
```